Salad Dressing Bottle Design

Looking for a design for front of salad dressing bottle. Must have sesame theme to be obvious

Australian theme.

Marlow Creek Sesame Dressing

Gluten Free
Vegan

100% Australian Grown Sesame Seeds
150gm

Colors
00AB8E
00BBA5
67D7C9
C6EFE9
E9F9F6
FFC000
F8CF3A
FAE287
FDF2CF
FEFAEE

```html
<!DOCTYPE html>
<html lang="en">
<head>
<meta charset="utf-8">
<title>Marlow Creek Sesame Dressing – Front Label</title>
<link href="https://fonts.googleapis.com/css2?family=Montserrat:wght@800&family=Oswald:wght@600&display=swap" rel="stylesheet">
<style>
  :root {
    --label-green: #00A887;
    --label-green-deep: #0C7A68;
    --sun-yellow: #F8CF3A;
    --text-white: #FFFFFF;
    --page-bg: #FFFFFF;
  }
  * { margin: 0; padding: 0; box-sizing: border-box; }
  html, body {
    width: 1200px;
    height: 1019px;
    overflow: hidden;
    background: var(--page-bg);
  }
  .label {
    position: absolute;
    left: 263px;
    top: 59px;
    width: 673px;
    height: 900px;
    background: var(--label-green);
    overflow: hidden;
  }
  .plant-artwork {
    position: absolute;
    left: 260px;
    top: 0;
    width: 413px;
    height: 900px;
    background: linear-gradient(100deg, rgba(12,122,104,0) 0%, rgba(12,122,104,0.22) 45%, rgba(12,122,104,0.38) 100%);
  }
  .logo-box {
    position: absolute;
    left: 88px;
    top: 59px;
    width: 242px;
    height: 59px;
    border: 2px solid var(--text-white);
    display: flex;
    align-items: center;
    justify-content: center;
    font-family: "Montserrat", sans-serif;
    font-weight: 800;
    font-size: 34px;
    color: var(--text-white);
    letter-spacing: 0.5px;
    white-space: nowrap;
  }
  .diet-badge {
    position: absolute;
    left: 470px;
    width: 160px;
    text-align: center;
    font-family: "Montserrat", sans-serif;
    font-weight: 800;
    font-size: 15.5px;
    line-height: 18px;
    color: var(--sun-yellow);
    white-space: nowrap;
  }
  .diet-badge svg { display: block; margin: 0 auto 8px; }
  .diet-badge--gluten { top: 31px; }
  .diet-badge--vegan { top: 153px; }
  .product-name {
    position: absolute;
    left: 82px;
    top: 262px;
    font-family: "Oswald", sans-serif;
    font-weight: 600;
    font-size: 107px;
    line-height: 107px;
    color: var(--sun-yellow);
    text-transform: uppercase;
    letter-spacing: 7px;
    white-space: nowrap;
  }
  .origin-claim {
    position: absolute;
    left: 84px;
    top: 726px;
    font-family: "Montserrat", sans-serif;
    font-weight: 800;
    font-size: 35px;
    line-height: 41px;
    color: var(--text-white);
    text-transform: uppercase;
    white-space: nowrap;
  }
  .net-weight {
    position: absolute;
    left: 84px;
    top: 837px;
    display: flex;
    align-items: center;
    gap: 4px;
    font-family: "Montserrat", sans-serif;
    font-weight: 800;
    font-size: 21px;
    color: var(--sun-yellow);
  }
  .net-weight::before {
    content: "";
    width: 8px;
    height: 16px;
    background: var(--sun-yellow);
  }
</style>
</head>
<body>
  <main class="label">
    <div class="plant-artwork" role="img" aria-label="Engraved line illustration of a flowering sesame plant with leaves and seed pods"></div>

    <div class="logo-box">YOUR LOGO</div>

    <div class="diet-badge diet-badge--gluten">
      <svg width="86" height="86" viewBox="0 0 88 88" fill="none" stroke="#F8CF3A" stroke-width="2.5" stroke-linecap="round" aria-hidden="true">
        <circle cx="44" cy="44" r="41"/>
        <line x1="15" y1="73" x2="73" y2="15"/>
        <line x1="44" y1="24" x2="44" y2="68"/>
        <path d="M44 26 q-5 5 0 10 q5 -5 0 -10z"/>
        <path d="M44 40 q-8 -4 -12 -10 q8 2 12 10z"/>
        <path d="M44 40 q8 -4 12 -10 q-8 2 -12 10z"/>
        <path d="M44 52 q-8 -4 -12 -10 q8 2 12 10z"/>
        <path d="M44 52 q8 -4 12 -10 q-8 2 -12 10z"/>
      </svg>
      GLUTEN FREE
    </div>

    <div class="diet-badge diet-badge--vegan">
      <svg width="86" height="86" viewBox="0 0 88 88" fill="none" stroke="#F8CF3A" stroke-width="2.5" stroke-linecap="round" stroke-linejoin="round" aria-hidden="true">
        <circle cx="44" cy="44" r="41"/>
        <path d="M26 34 L40 64 L52 34"/>
        <path d="M48 44 q2 -16 18 -20 q0 16 -16 20z"/>
        <line x1="50" y1="42" x2="60" y2="30"/>
      </svg>
      VEGAN
    </div>

    <h1 class="product-name">Marlow<br>Creek<br>Sesame<br>Dressing</h1>

    <p class="origin-claim">100% Australian<br>Grown Sesame Seeds</p>

    <p class="net-weight">150GM</p>
  </main>
</body>
</html>
```